Calling All Web Design Visionaries: Transform the Meridian Vault Website!

Dear Web Design Innovators,

Are you ready to embark on a cosmic design journey? We are thrilled to announce an exciting opportunity to revamp and upgrade the Meridian Vault website, and we need your exceptional design prowess to bring our vision to life.

About Meridian Vault:
Meridian Vault is on a mission to reshape the future of space construction. We're pioneers in the field, developing cutting-edge concept construction blocks that promise to redefine how we build beyond our planet's boundaries. Our solutions are scalable, sustainable, and poised to accelerate humanity's journey into the cosmos.

Current Website:
Take a look at our current website [www.meridianvault-example.co.uk](https://www.meridianvault-example.co.uk) to get a glimpse of our existing online presence. While it served us well, we believe it's time for a transformative makeover.

Your Mission:
We're seeking imaginative web designers who can bring a fresh perspective to our online platform. Here's the website layout we're envisioning:
- Homepage: A futuristic and clean design that reflects our commitment to innovation. Clear navigation to key sections.
- About Us: A captivating section introducing our mission and team.
- Products: Highlighting our revolutionary concept construction blocks.
- Projects: Showcasing our involvement in space construction initiatives.
- Blog: A space to share our insights, progress, and news.
- Contact: Easy access for potential partners and investors to reach out.

Image Suggestions:
- Celestial imagery, cosmic landscapes, and space construction concepts can add a captivating visual element.
- Incorporate a color palette that combines deep space blues with modern metallic tones for a futuristic feel.
- Use high-quality images and graphics that convey the excitement and possibilities of space construction.

Why You Should Join Us:
By taking on this challenge, you'll have the chance to contribute to a groundbreaking mission and be part of the future of space exploration. Your design will be seen by space enthusiasts, investors, and industry experts worldwide.

If you're ready to embark on this cosmic design journey with us, please submit your portfolio and a brief introduction by 22/09/23. We can't wait to see your visionary concepts.

Let's transform the Meridian Vault website into a space of inspiration and innovation. Join us on this incredible adventure!

Best regards,

Tobi
Updates

Target Market(s)

Orbit Service providers, Governments, Space Agencies. Space Infrastructure

Industry/Entity Type

Space, Technology, Innovation, Architecture. Construction

Coding

Coded - Design and coding required

Number of Pages Required

5+ page

Colors
0054AA
0677BA
7BADD7
CADEEF
E8F1F8
6B429C
8869AF
B7A5CE
E3DAEB
F3F0F8

Requirements
Must have
• The logos i have outlined in the website revamp doc, i also need a sub section for FAQs terms of service etc like most professional websites. A page to sell merch. Like our custom hoody, t shirt, key rings, hats, joggers, etc
Nice to have
• any case studies of satellite innovations reaching project completion and how they might relate to my project.

```html
<!DOCTYPE html>
<html lang="en">
<head>
<meta charset="UTF-8">
<title>Meridian Vault — Invest in the Future</title>
<link href="https://fonts.googleapis.com/css2?family=Exo+2:ital,wght@0,400;0,500;0,600;0,700;1,500;1,600&display=swap" rel="stylesheet">
<style>
:root{
  --space:#000000;
  --card:#14141f;
  --accent:#2f2ff0;
  --accent-soft:#4c3cf5;
  --white:#ffffff;
  --muted:#a9a9b6;
  --logo-grey:#9a9aa3;
}
*{margin:0;padding:0;box-sizing:border-box}
html,body{width:1200px;height:2879px;overflow:hidden;background:var(--space)}
body{font-family:"Exo 2",sans-serif;color:var(--white);position:relative}
.abs{position:absolute}
.center{left:0;width:1200px;text-align:center}

/* hero */
.hero{position:absolute;left:0;top:0;width:1200px;height:582px;overflow:hidden;background:#000}
.hero-scene{position:absolute;inset:0;
  background:radial-gradient(ellipse 640px 330px at 600px 560px,rgba(40,80,160,.75),rgba(15,30,70,.45) 55%,transparent 80%),
  radial-gradient(ellipse 400px 160px at 600px 400px,rgba(70,130,230,.35),transparent 70%),
  linear-gradient(180deg,#000 0%,#03060f 55%,#0a1430 100%)}
.logo{position:absolute;left:67px;top:56px;display:flex;align-items:center;gap:10px}
.logo-mark{width:22px;height:22px;background:var(--logo-grey)}
.logo-name{font-weight:700;font-size:22px;color:var(--logo-grey);letter-spacing:.5px}
.nav{position:absolute;top:71px;font-weight:600;font-size:13px;letter-spacing:.3px}
.nav a{position:absolute;color:var(--white);text-decoration:none;white-space:nowrap}
.nav a.active{color:var(--accent-soft)}
.search{position:absolute;left:1018px;top:63px;width:115px;height:32px;border:1.5px solid var(--white);border-radius:16px;
  display:flex;align-items:center;justify-content:center;gap:7px;font-weight:600;font-size:13px}
.hero-title{top:152px;font-weight:700;font-size:50px;letter-spacing:.5px}
.hero-sub{top:218px;font-size:34px;font-weight:400}
.hero-text{top:274px;left:360px;width:480px;text-align:center;font-size:17px;line-height:20px}
.btn{position:absolute;background:var(--accent);color:var(--white);font-weight:600;font-size:13px;
  display:flex;align-items:center;justify-content:center;gap:9px;border-radius:3px}
.badge{position:absolute;left:903px;top:378px;width:100px;height:100px;border-radius:50%;border:2px solid #6d6d78}

/* decorative fills */
.deco{position:absolute}
.orbit-ornament{left:505px;top:600px;width:225px;height:122px;
  background:radial-gradient(ellipse 110px 55px at 50% 50%,rgba(255,255,255,.10),transparent 75%)}
.aurora{left:0;top:1120px;width:520px;height:230px;
  background:radial-gradient(ellipse 260px 80px at 260px 110px,rgba(31,122,62,.45),transparent 75%)}
.purple-haze{left:900px;top:740px;width:300px;height:360px;
  background:radial-gradient(ellipse 150px 170px at 200px 180px,rgba(90,60,220,.35),transparent 75%)}
.planet-area{left:900px;top:1180px;width:300px;height:400px;
  background:radial-gradient(ellipse 170px 200px at 220px 200px,rgba(90,99,216,.75),rgba(46,53,144,.4) 60%,transparent 85%)}
.sphere-area{left:60px;top:1280px;width:470px;height:470px;
  background:radial-gradient(ellipse 230px 230px at 45% 45%,rgba(40,40,140,.28),transparent 80%)}

/* intro */
.orbit-ring{position:absolute;left:360px;top:857px;width:336px;height:336px;border-radius:50%;border:1.5px solid #2a2a34}
.intro-photo{position:absolute;left:70px;top:671px;width:518px;height:458px;border-radius:8px;
  background:linear-gradient(160deg,#dfe6ee 0%,#8da3bd 35%,#3d5678 70%,#1a2b45 100%)}
.quote-card{position:absolute;left:330px;top:926px;width:332px;height:150px;border-radius:14px;background:var(--card);
  display:flex;align-items:center;gap:22px;padding-left:36px}
.quote-card p{font-style:italic;font-weight:600;font-size:25px;line-height:34px}
.section-title{font-weight:700;font-size:34px;letter-spacing:.3px}
.rule{position:absolute;height:3px;width:64px;background:var(--accent)}
.intro-copy{position:absolute;left:713px;top:818px;width:430px;font-size:13.5px;line-height:20px;color:#e8e8ee}
.intro-copy p{margin-bottom:20px}

/* features */
.features-text{top:1412px;left:355px;width:490px;text-align:center;font-size:17.5px;line-height:20px}
.feature-card{position:absolute;top:1553px;width:241px;height:348px;background:var(--card);border-radius:12px;
  text-align:center;padding:22px 18px 0}
.feature-card svg{display:block;margin:0 auto 12px}
.feature-card h3{font-weight:700;font-size:19px;line-height:22px;margin-bottom:10px}
.feature-card p{font-size:13px;line-height:16px;color:var(--muted)}
.dash{position:absolute;top:1944px;width:29px;height:3px;background:#d0d0d8}

/* newsletter */
.horizon{position:absolute;left:0;top:2150px;width:1200px;height:420px;
  background:radial-gradient(ellipse 900px 300px at 600px 380px,rgba(25,45,95,.85),rgba(15,28,60,.5) 60%,transparent 85%)}
.satellite{position:absolute;left:231px;top:2061px;width:751px;height:184px;
  background:linear-gradient(90deg,#22304f 0%,#2c3a5e 40%,#e8e8ea 48%,#bfc2c8 55%,#2c3a5e 60%,#22304f 100%)}
.email{position:absolute;left:250px;top:2484px;width:700px;height:65px;border-radius:33px;background:var(--white);
  color:#222;font-style:italic;font-weight:500;font-size:17px;display:flex;align-items:center;padding-left:33px}
.email span{color:#e33;margin-left:4px}
.social{position:absolute;top:2705px;width:47px;height:47px;border-radius:50%;border:1.5px solid var(--white);
  display:flex;align-items:center;justify-content:center;font-size:10px;font-weight:600;color:var(--white)}
.footer{top:2797px;font-size:13px;color:#c8c8d2}
</style>
</head>
<body>

<header class="hero">
  <div class="hero-scene" role="img" aria-label="Night-side view of Earth glowing below a starry sky"></div>
  <div class="logo"><span class="logo-mark"></span><span class="logo-name">Meridian Vault</span></div>
  <nav class="nav">
    <a class="active" style="left:451px">HOME</a>
    <a style="left:532px">ABOUT US</a>
    <a style="left:637px">PRODUCTS</a>
    <a style="left:746px">PROJECTS</a>
    <a style="left:851px">BLOG</a>
    <a style="left:926px">CONTACT</a>
  </nav>
  <div class="search">
    <svg width="12" height="12" viewBox="0 0 12 12" fill="none" stroke="#fff" stroke-width="1.6"><circle cx="5" cy="5" r="3.8"/><path d="M8 8l3 3"/></svg>Search
  </div>
  <h1 class="abs center hero-title">INVEST IN THE FUTURE</h1>
  <h2 class="abs center hero-sub">Dare to Dream, Dare to Invest</h2>
  <p class="abs hero-text">A new frontier beckons, and it's unlike anything humanity has ever witnessed. The possibilities are boundless, the horizons limitless. Are you ready to join the voyage into the future?</p>
  <a class="btn" style="left:533px;top:360px;width:126px;height:39px">Learn More
    <svg width="7" height="11" viewBox="0 0 7 11" fill="none" stroke="#fff" stroke-width="1.6"><path d="M1 1l4.5 4.5L1 10"/></svg></a>
  <div class="badge" aria-label="Company badge"></div>
</header>

<div class="deco aurora" role="img" aria-label="Green aurora glow"></div>
<div class="deco purple-haze" role="img" aria-label="Purple nebula glow"></div>
<div class="deco sphere-area" role="img" aria-label="Dotted particle globe in deep blue"></div>
<div class="deco planet-area" role="img" aria-label="Blue gas giant planet at the right edge"></div>
<div class="deco orbit-ornament" role="img" aria-label="Dashed orbit path ornament with arrow"></div>

<div class="orbit-ring"></div>
<div class="intro-photo" role="img" aria-label="Spacecraft module orbiting above clouded Earth"></div>
<div class="quote-card">
  <svg width="50" height="50" viewBox="0 0 50 50" fill="none" stroke="#fff" stroke-width="1.8">
    <rect x="14" y="8" width="20" height="20" rx="2"/><rect x="19" y="13" width="10" height="10" stroke="#5b5bff"/>
    <path d="M4 36c8 0 12 4 20 4h14l8-6M4 44h26l16-8" stroke="#5b5bff"/>
  </svg>
  <p>“If you build it,<br>they will come”</p>
</div>
<div class="abs" style="left:580px;top:1146px;width:42px;height:42px;border-radius:50%;background:var(--accent-soft)"></div>
<div class="abs" style="left:624px;top:1187px;width:9px;height:9px;border-radius:50%;background:#fff"></div>

<h2 class="abs section-title" style="left:713px;top:742px">INTRODUCTION</h2>
<div class="rule" style="left:713px;top:789px"></div>
<div class="intro-copy">
  <p>Redefining the Boundaries of Space</p>
  <p>In an industry where history and reputation often take centre stage, we're the fresh face poised to redefine the rules. Meet The Meridian Vault—a newcomer with a vision that's nothing short of revolutionary.</p>
  <p>A New Era Unfolds: We might not have a long history, but we're here to create one. Our mission is simple: to bridge the gap between everyday business and the cosmos. No longer is space a distant realm reserved solely for 'space companies.' We're making it a seamless extension of industry itself.</p>
</div>
<a class="btn" style="left:713px;top:1082px;width:126px;height:41px">Learn More
  <svg width="7" height="11" viewBox="0 0 7 11" fill="none" stroke="#fff" stroke-width="1.6"><path d="M1 1l4.5 4.5L1 10"/></svg></a>

<h2 class="abs center section-title" style="top:1272px">KEY FEATURES</h2>
<div class="rule" style="left:568px;top:1320px"></div>
<h3 class="abs center" style="top:1350px;font-weight:400;font-size:34px">Pioneering the Cosmos</h3>
<p class="abs features-text">Imagine standing at the threshold of a brand-new frontier, one that stretches far beyond the boundaries of our earthly existence. It's a realm where the possibilities are as limitless as the stars themselves.</p>

<article class="feature-card" style="left:67px">
  <svg width="56" height="56" viewBox="0 0 56 56" fill="none" stroke="#fff" stroke-width="1.8"><path d="M46 8c-12 0-22 8-28 20l10 10c12-6 20-16 18-30z"/><circle cx="35" cy="20" r="4" stroke="#5b5bff"/><path d="M18 28l-8 2-4 6 10-1M28 38l-2 8-6 4 1-10M14 42l-6 8"/></svg>
  <h3>The Space Odyssey Begins</h3>
  <p>The space industry is amid an exhilarating renaissance. Every day, new companies emerge, ushering in a future where space operations become as commonplace as a morning commute. This is the onset of a modern-day gold rush—a cosmic opportunity like no other.</p>
</article>
<article class="feature-card" style="left:342px">
  <svg width="56" height="56" viewBox="0 0 56 56" fill="none" stroke="#fff" stroke-width="1.8"><path d="M20 4L8 30h12l-4 20 16-26H22z"/><circle cx="38" cy="38" r="9" stroke="#5b5bff"/><path d="M33 38c2-3 4-3 5 0s3 3 5 0" stroke="#5b5bff"/></svg>
  <h3>Endless Resources, Infinite Energy</h3>
  <p>In space, we're not just discovering resources; we're unlocking a treasure trove of possibilities. The potential to harness phenomenal solar energy and tap into vast cosmic riches is within reach. It's a new era, reminiscent of the explorations that ignited humanity's journey across uncharted waters.</p>
</article>
<article class="feature-card" style="left:617px">
  <svg width="56" height="56" viewBox="0 0 56 56" fill="none" stroke="#fff" stroke-width="1.8"><circle cx="27" cy="29" r="23"/><circle cx="27" cy="29" r="15"/><circle cx="27" cy="29" r="7" stroke="#5b5bff"/><path d="M27 29L46 10M42 6v8h8" stroke="#5b5bff"/></svg>
  <h3>A Market Set<br>to Soar</h3>
  <p>As we embark on this cosmic adventure, the market is poised for exponential growth, mirroring the explosive expansion of opportunities that accompanied the discovery of the New World. Space and technology revolutions converge, creating a spectacle of wonder, awe, and boundless splendour.</p>
</article>
<article class="feature-card" style="left:891px">
  <svg width="56" height="56" viewBox="0 0 56 56" fill="none" stroke="#fff" stroke-width="1.8"><circle cx="28" cy="8" r="5" stroke="#5b5bff"/><path d="M20 24c0-6 16-6 16 0" stroke="#5b5bff"/><path d="M6 12v22l10 10v8M50 12v22L40 44v8M12 20v12l8 6M44 20v12l-8 6M16 52h8M32 52h8"/></svg>
  <h3>A New Paradigm for Humanity</h3>
  <p>We stand on the precipice of a new era, a paradigm shift that transcends the boundaries of our imagination. With the financial backing to support our dreams, the entire solar system becomes our backyard, waiting to be explored and transformed.</p>
</article>
<div class="dash" style="left:540px;background:var(--accent)"></div>
<div class="dash" style="left:585px"></div>
<div class="dash" style="left:631px"></div>

<div class="horizon" role="img" aria-label="Earth horizon glowing blue at the edge of space"></div>
<div class="satellite" role="img" aria-label="Satellite with extended solar panel arrays"></div>

<h2 class="abs center section-title" style="top:2335px">JOIN OUR NEWSLETTER</h2>
<div class="rule" style="left:568px;top:2384px"></div>
<p class="abs center" style="top:2410px;font-style:italic;font-weight:500;font-size:22px">Keep informed of the updates</p>
<div class="email">Enter your email<span>*</span></div>
<a class="btn" style="left:516px;top:2588px;width:167px;height:49px;border-radius:25px">Subscribe
  <svg width="7" height="11" viewBox="0 0 7 11" fill="none" stroke="#fff" stroke-width="1.6"><path d="M1 1l4.5 4.5L1 10"/></svg></a>

<a class="social" style="left:491px">Chirp</a>
<a class="social" style="left:548px">Folio</a>
<a class="social" style="left:605px">Lenso</a>
<a class="social" style="left:662px">Nexa</a>

<p class="abs center footer">Copyright © 2023 Meridian Vault. All Rights Reserved | Terms &amp; Conditions</p>

</body>
</html>
```